It is a leisure sector investment company.The company plans to invest in a luxurious 5 star resort

We need a stationery design to our company 'Copper Lantern Limited' using the winning logo design. We need the letter heads, envelopes & the business cards. Should be simple, plain and professional
We have upload the source file & vector files which gives our logo design. We prefer the bottom logo.

Have updated under 'must have priorities', the company name, address, tel no. fax no. & the company reg no. which should come on the letter head. the long envelope should have the company name, tel & fax no. 
Business card should have the company name, name on the card, designation, tel no. fax no.  

- Letter head details:
Copper Lantern Limited
14 Floor, South Wing, Halvard Merchant Plaza,
Merrow Court, Colombo 01, Sri Lanka
Tel: +94 11 5047293 Fax: +94 11 5047298
Company Reg No.QX 6142
Long Envelope should have only the company name, adress, Tel & Fax
Business Cards should have the company name, Tel & Fax:
Business Card 1 - Lasantha Gunaratne - Chairman
Business Card 2 - Nimal.T.Wijesooriya - COO

```html
<!DOCTYPE html>
<html lang="en">
<head>
<meta charset="utf-8">
<title>Copper Lantern Limited — Stationery</title>
<link href="https://fonts.googleapis.com/css2?family=Marcellus&family=Cabin:wght@400;600&display=swap" rel="stylesheet">
<style>
  :root{
    --backdrop:#e3e3e3;
    --paper:#ffffff;
    --paper-shade:#f3f3f3;
    --copper:#6d5c54;
    --copper-dark:#54463f;
    --rule-grey:#b9b9b9;
    --fold-grey:#dedede;
    --ink:#3a3a3a;
    --ink-soft:#5a5a5a;
    --window:#efefef;
    --pattern:#f1f1f1;
  }
  *{box-sizing:border-box;margin:0;padding:0}
  html,body{width:1200px;height:808px;overflow:hidden}
  body{background:var(--backdrop);position:relative;font-family:"Cabin",sans-serif;color:var(--ink)}

  .sheet{position:absolute;background:var(--paper);box-shadow:0 2px 6px rgba(0,0,0,.18);overflow:hidden}

  .wordmark{font-family:"Marcellus",serif;color:var(--copper);text-align:center;font-weight:400;line-height:1}
  .wordmark .symbol{display:block;margin:0 auto;border-radius:50%;background:var(--copper)}
  .wordmark .name{display:block;letter-spacing:.02em}
  .wordmark .suffix{display:block;letter-spacing:.35em}

  .faint-pattern{position:absolute;background:radial-gradient(ellipse at center,var(--pattern) 0%,rgba(255,255,255,0) 70%)}

  .footer-band{position:absolute;left:0;right:0;bottom:0;background:var(--copper)}
  .footer-band::before{content:"";position:absolute;left:0;right:0;top:-5px;height:2px;background:var(--rule-grey)}

  .contact-line{display:flex;justify-content:center;align-items:center;gap:5px;color:var(--ink-soft)}
  .contact-line svg{width:8px;height:8px;flex:none}

  /* Letterhead */
  .letterhead{left:30px;top:22px;width:540px;height:764px}
  .letterhead .wordmark{position:relative;margin-top:30px}
  .letterhead .wordmark .symbol{width:24px;height:24px;margin-bottom:8px}
  .letterhead .wordmark .name{font-size:25px}
  .letterhead .wordmark .suffix{font-size:13px;margin-top:3px}
  .letterhead .address{position:relative;margin-top:8px;text-align:center;font-size:7.5px;color:var(--ink-soft);line-height:1.5}
  .letterhead .contact-line{position:relative;font-size:7.5px}
  .letterhead .faint-pattern{left:150px;bottom:30px;width:340px;height:240px}
  .letter-body{position:absolute;left:60px;right:58px;top:190px;font-size:9.6px;line-height:1.55;color:var(--ink)}
  .letter-date{margin-bottom:20px}
  .recipient{margin-bottom:22px;line-height:1.45}
  .recipient .person{font-weight:600;font-size:11px}
  .recipient .firm{font-weight:600}
  .letter-body p{text-align:justify;margin-bottom:12px}
  .sign-off{margin-top:16px}
  .signature{width:110px;height:46px;margin:10px 0 6px;background:linear-gradient(135deg,#f2f2f2,#dcdcdc);border-radius:3px}
  .signer .person{font-weight:600}
  .letterhead .footer-band{height:22px}

  /* Business cards */
  .card{top:20px;width:270px;height:148px}
  .card-front{left:600px}
  .card-front .wordmark{margin-top:16px}
  .card-front .wordmark .symbol{width:14px;height:14px;margin-bottom:6px}
  .card-front .wordmark .name{font-size:17px}
  .card-front .wordmark .suffix{font-size:9px;margin-top:2px}
  .card-holder{margin-top:10px;text-align:center;font-family:"Marcellus",serif;font-size:8px;color:var(--ink-soft);line-height:1.5;letter-spacing:.03em}
  .card-front .contact-line{position:absolute;left:0;right:0;bottom:20px;font-size:7px}
  .card-front .footer-band{height:10px}
  .card-back{left:900px;background:var(--copper);display:flex;align-items:center;justify-content:center}
  .card-back .wordmark{color:var(--paper)}
  .card-back .wordmark .symbol{width:16px;height:16px;margin-bottom:7px;background:var(--paper)}
  .card-back .wordmark .name{font-size:19px}
  .card-back .wordmark .suffix{font-size:10px;margin-top:3px}

  /* Envelope, back with flap */
  .envelope-back{left:600px;top:186px;width:570px;height:120px}
  .envelope-back svg{position:absolute;inset:0;width:100%;height:100%}

  /* Long envelope, front */
  .envelope{left:600px;top:324px;width:570px;height:240px}
  .envelope-brand{position:absolute;left:54px;top:26px;width:210px}
  .envelope .wordmark .symbol{width:18px;height:18px;margin-bottom:7px}
  .envelope .wordmark .name{font-size:20px}
  .envelope .wordmark .suffix{font-size:11px;margin-top:3px}
  .envelope .contact-line{margin-top:9px;font-size:7px}
  .envelope .faint-pattern{left:300px;top:60px;width:240px;height:160px}
  .address-window{position:absolute;left:54px;top:128px;width:262px;height:72px;border-radius:8px;background:var(--window);box-shadow:inset 0 1px 3px rgba(0,0,0,.15)}
  .envelope .footer-band{height:16px}

  /* Brand panel */
  .brand-panel{left:600px;top:582px;width:570px;height:204px;display:flex;align-items:center;justify-content:center;background:linear-gradient(180deg,var(--paper),var(--paper-shade))}
  .brand-panel .wordmark .symbol{width:30px;height:30px;margin-bottom:12px}
  .brand-panel .wordmark .name{font-size:36px}
  .brand-panel .wordmark .suffix{font-size:19px;margin-top:6px}
</style>
</head>
<body>

<svg width="0" height="0" style="position:absolute" aria-hidden="true">
  <symbol id="icon-phone" viewBox="0 0 10 10">
    <circle cx="5" cy="5" r="5" fill="#6d5c54"/>
    <path d="M3.2 2.6c.3-.2.6-.2.8.1l.5.8c.1.2 0 .5-.2.6l-.3.2c.3.6.7 1 1.3 1.3l.2-.3c.1-.2.4-.3.6-.2l.8.5c.3.2.3.5.1.8-.4.5-1 .6-1.6.3C4.2 6.1 3.3 5.2 2.8 4c-.2-.6 0-1.1.4-1.4z" fill="#fff"/>
  </symbol>
  <symbol id="icon-fax" viewBox="0 0 10 10">
    <circle cx="5" cy="5" r="5" fill="#6d5c54"/>
    <rect x="2.6" y="4" width="4.8" height="2.8" rx=".4" fill="#fff"/>
    <rect x="3.5" y="2.5" width="3" height="1.8" fill="#fff"/>
  </symbol>
</svg>

<!-- Letterhead -->
<section class="sheet letterhead">
  <div class="faint-pattern" role="img" aria-label="Faint decorative flourish pattern"></div>
  <div class="wordmark"><span class="symbol" role="img" aria-label="Company symbol"></span><span class="name">COPPER LANTERN</span><span class="suffix">LIMITED</span></div>
  <div class="address">14 Floor, South Wing, Halvard Merchant Plaza, Merrow Court, Colombo 01, Sri Lanka</div>
  <div class="contact-line">
    <svg><use href="#icon-phone"/></svg><span>+94 11 5047293</span>
    <svg><use href="#icon-fax"/></svg><span>+94 11 5047298</span>
    <span>Company Reg No. QX 6142</span>
  </div>

  <div class="letter-body">
    <div class="letter-date">March 4, 2011</div>
    <div class="recipient">
      <div class="person">Mr Owen Hartley</div>
      <div>Managing Director</div>
      <div class="firm">Meridian Harbor Investors</div>
      <div>48 W Cedar Avenue</div>
      <div>Larkfield, WA 98702</div>
    </div>
    <p>Lorem Ipsum is simply dummy text of the printing and typesetting industry. Lorem Ipsum has been the industry's standard dummy text ever since the 1500s, when an unknown printer took a galley of type and scrambled it to make a type specimen book. It has survived not only five centuries, but also the leap into electronic typesetting, remaining essentially unchanged. It was popularised in the 1960s with the release of Pressline sheets containing Lorem Ipsum passages, and more recently with desktop publishing software like Folio PageSetter including versions of Lorem Ipsum.</p>
    <p>Contrary to popular belief, Lorem Ipsum is not simply random text. It has roots in a piece of classical Latin literature from 45 BC, making it over 2000 years old. Rowan Ellery, a Latin professor at Ashcombe College in Virginia, looked up one of the more obscure Latin words, consectetur, from a Lorem Ipsum passage, and going through the cites of the word in classical literature, discovered the undoubtable source. Lorem Ipsum comes from sections 1.10.32 and 1.10.33 of "de Finibus Bonorum et Malorum" (The Extremes of Good and Evil) by Aurelian Sextus, written in 45 BC. This book is a treatise on the theory of ethics, very popular during the Renaissance. The first line of Lorem Ipsum, "Lorem ipsum dolor sit amet..", comes from a line in section 1.10.32.</p>
    <div class="sign-off">Thank You for being one of our valued customers.</div>
    <div class="signature" role="img" aria-label="Handwritten signature of Teodor Valen"></div>
    <div class="signer">
      <div class="person">Teodor Valen</div>
      <div>President</div>
      <div>Larkfield Fabrication</div>
    </div>
  </div>
  <div class="footer-band"></div>
</section>

<!-- Business card, front -->
<section class="sheet card card-front">
  <div class="wordmark"><span class="symbol" role="img" aria-label="Company symbol"></span><span class="name">COPPER LANTERN</span><span class="suffix">LIMITED</span></div>
  <div class="card-holder">Lasantha Gunaratne<br>Chairman</div>
  <div class="contact-line">
    <svg><use href="#icon-phone"/></svg><span>+94 11 5047293</span>
    <svg><use href="#icon-fax"/></svg><span>+94 11 5047298</span>
  </div>
  <div class="footer-band"></div>
</section>

<!-- Business card, back -->
<section class="sheet card card-back">
  <div class="wordmark"><span class="symbol" role="img" aria-label="Company symbol"></span><span class="name">COPPER LANTERN</span><span class="suffix">LIMITED</span></div>
</section>

<!-- Envelope, back with flap -->
<section class="sheet envelope-back">
  <svg viewBox="0 0 570 120" preserveAspectRatio="none" aria-hidden="true">
    <path d="M0 120 L250 66 M570 120 L330 66" stroke="var(--fold-grey)" stroke-width="1" fill="none"/>
    <path d="M0 0 H570 V22 C470 40 380 78 285 84 C190 78 100 40 0 22 Z" fill="var(--copper)"/>
  </svg>
  <span role="img" aria-label="Company symbol on flap" style="position:absolute;left:276px;top:30px;width:18px;height:18px;border-radius:50%;background:var(--paper)"></span>
</section>

<!-- Long envelope, front -->
<section class="sheet envelope">
  <div class="faint-pattern" role="img" aria-label="Faint decorative flourish pattern"></div>
  <div class="envelope-brand">
    <div class="wordmark"><span class="symbol" role="img" aria-label="Company symbol"></span><span class="name">COPPER LANTERN</span><span class="suffix">LIMITED</span></div>
    <div class="contact-line">
      <svg><use href="#icon-phone"/></svg><span>+94 11 5047293</span>
      <svg><use href="#icon-fax"/></svg><span>+94 11 5047298</span>
    </div>
  </div>
  <div class="address-window"></div>
  <div class="footer-band"></div>
</section>

<!-- Brand panel -->
<section class="sheet brand-panel">
  <div class="wordmark"><span class="symbol" role="img" aria-label="Company symbol"></span><span class="name">COPPER LANTERN</span><span class="suffix">LIMITED</span></div>
</section>

</body>
</html>
```